Business Card Design

New business card design

Target Market(s)

Residential & Commercial Property Managers

Industry/Entity Type

Plumbing Services

Contact Information for Business Card

Name - Owen Tredgold, title - Director, Phone Number - 0431 862 507, email - owen@rvb-plumbing.com.au, Company ABN - 73 215 904 386,

Font styles to use
Sans Serif

Colors
0054AA
0677BA
7BADD7
CADEEF
E8F1F8

```html
<!DOCTYPE html>
<html lang="en">
<head>
<meta charset="utf-8">
<title>RVB Plumbing Services – Business Card</title>
<link rel="stylesheet" href="https://fonts.googleapis.com/css2?family=Montserrat:wght@600&family=Questrial&display=swap">
<style>
  :root {
    --page-bg: #3a3b3d;
    --card-white: #f7f8f9;
    --ink-dark: #1c2a33;
    --brand-blue: #1a9ad6;
    --brand-mid: #0677ba;
    --band-dark: #1d3441;
    --band-deep: #16252e;
    --line-soft: #7badd7;
    --text-grey: #3a3f44;
  }
  * { box-sizing: border-box; margin: 0; padding: 0; }
  html, body { width: 1200px; height: 900px; overflow: hidden; }
  body {
    background: var(--page-bg);
    position: relative;
    font-family: "Questrial", sans-serif;
  }
  .card {
    position: absolute;
    box-shadow: 0 14px 30px rgba(0,0,0,0.45);
    overflow: hidden;
  }
  /* Front (portrait) */
  .card-front {
    left: 150px; top: 160px;
    width: 340px; height: 580px;
    background: linear-gradient(90deg, var(--band-deep) 0%, var(--band-dark) 30%, var(--brand-blue) 62%, var(--band-dark) 90%, var(--band-deep) 100%);
  }
  .card-front .face-shape { position: absolute; inset: 0; }
  .front-content {
    position: absolute; inset: 0;
    text-align: center;
    color: var(--text-grey);
  }
  .wordmark {
    position: absolute; left: 0; right: 0; top: 70px;
    font-family: "Questrial", sans-serif;
    color: var(--ink-dark);
  }
  .wordmark-main { font-size: 64px; letter-spacing: 2px; line-height: 1; }
  .wordmark-sub { font-size: 12px; letter-spacing: 6px; margin-top: 8px; }
  .person-name {
    position: absolute; left: 0; right: 0; top: 212px;
    font-family: "Montserrat", sans-serif; font-weight: 600;
    font-size: 19px; color: var(--ink-dark);
  }
  .person-title {
    position: absolute; left: 0; right: 0; top: 238px;
    font-size: 15px; color: var(--brand-blue);
  }
  .contact-divider {
    position: absolute; left: 30px; right: 30px; top: 330px;
    display: flex; align-items: center; gap: 10px;
  }
  .contact-divider .rule { flex: 1; height: 1px; background: var(--line-soft); opacity: .6; }
  .contact-icon {
    width: 26px; height: 26px; border-radius: 50%;
    background: var(--brand-blue);
    display: flex; align-items: center; justify-content: center;
  }
  .contact-lines {
    position: absolute; left: 0; right: 0; top: 372px;
    font-size: 14.5px; line-height: 1; color: var(--text-grey);
  }
  .contact-lines p { margin-bottom: 20px; }
  .contact-lines .abn { margin-top: 36px; }
  /* Back (landscape) */
  .card-back {
    left: 570px; top: 280px;
    width: 580px; height: 340px;
    background: linear-gradient(90deg, var(--band-deep) 0%, var(--band-dark) 25%, var(--brand-blue) 52%, var(--band-dark) 82%, var(--band-deep) 100%);
    display: flex; flex-direction: column; align-items: center; justify-content: center;
    color: #ffffff;
  }
  .card-back .wordmark-main { font-size: 70px; }
  .card-back .wordmark-sub { font-size: 12px; }
</style>
</head>
<body>

<section class="card card-front" aria-label="Business card front">
  <svg class="face-shape" width="340" height="580" viewBox="0 0 340 580" aria-hidden="true">
    <path d="M0 0 H340 V330 C340 470 280 545 180 545 C100 545 40 500 0 420 Z" fill="#0f1a20"/>
    <path d="M0 0 H340 V322 C338 460 278 538 180 538 C102 538 42 494 0 414 Z" fill="var(--card-white)"/>
  </svg>
  <div class="front-content">
    <div class="wordmark">
      <div class="wordmark-main">rvb</div>
      <div class="wordmark-sub">plumbing services</div>
    </div>
    <h1 class="person-name">Owen Tredgold</h1>
    <p class="person-title">Director</p>
    <div class="contact-divider">
      <span class="rule"></span>
      <span class="contact-icon" aria-label="Phone">
        <svg width="14" height="14" viewBox="0 0 24 24"><path fill="#fff" d="M6.6 10.8a15 15 0 0 0 6.6 6.6l2.2-2.2a1 1 0 0 1 1-.25 11.4 11.4 0 0 0 3.6.57 1 1 0 0 1 1 1V20a1 1 0 0 1-1 1A17 17 0 0 1 3 4a1 1 0 0 1 1-1h3.5a1 1 0 0 1 1 1c0 1.25.2 2.45.57 3.6a1 1 0 0 1-.25 1z"/></svg>
      </span>
      <span class="contact-icon" aria-label="Email">
        <svg width="14" height="14" viewBox="0 0 24 24"><rect x="2" y="5" width="20" height="14" rx="1.5" fill="none" stroke="#fff" stroke-width="2"/><path d="M3 6l9 7 9-7" fill="none" stroke="#fff" stroke-width="2"/></svg>
      </span>
      <span class="rule"></span>
    </div>
    <div class="contact-lines">
      <p>0431 862 507</p>
      <p>owen@rvb-plumbing.com.au</p>
      <p class="abn">ABN - 73 215 904 386</p>
    </div>
  </div>
</section>

<section class="card card-back" aria-label="Business card back">
  <div class="wordmark-main">rvb</div>
  <div class="wordmark-sub">plumbing services</div>
</section>

</body>
</html>
```